VALMIK GROUP

This is a company that provides executive protection. Our motto is "New Era in Protection"... I don't want this to look like other security websites. I want it to be clean and sharp and represent a new era. We are based in the bay area so maybe a picture of San Francisco in the background?
I want it to be able to funnel down a couple different categories.
1. About Us
2. Services (Executive Protection, Covert Protection, Residential Protection & Intelligence)
3. Blue Pike (Training & Consulting)
4. Contact Us
I want it to be very clean and modern. I don't want there to be any pictures of bodyguards with ear pieces like every other website.
Target Market(s)
Ultra High Net Worth Individuals
Coding
Coded - Design and coding required
Number of Pages Required
1 page
Requirements
Must have
- Colors of my Symbol
Nice to have
- City in the background, San Francisco, New York or the Thornmeadow Club in Montana.
Should not have
- Should not look like an KVM website or have photos of bodyguards. I want this to be a clean and simple website with my logo

```html
<!DOCTYPE html>
<html lang="en">
<head>
<meta charset="utf-8">
<title>VALMIK GROUP — New Era in Protection</title>
<link href="https://fonts.googleapis.com/css2?family=Poppins:wght@200;300;400;500;600;700;800&display=swap" rel="stylesheet">
<style>
:root{
  --red:#8e1418;
  --red-deep:#6f0f12;
  --ink:#141414;
  --text:#555;
  --muted:#777;
  --white:#fff;
  --dusk-top:#2a2140;
  --dusk-mid:#3d3158;
  --city-glow:#b8743a;
  --wood:#2a1814;
}
*{margin:0;padding:0;box-sizing:border-box}
html,body{width:1200px;height:3396px;overflow:hidden;background:var(--white)}
body{font-family:'Poppins',sans-serif;color:var(--ink);position:relative}
.abs{position:absolute}
/* header */
.brand{position:absolute;display:flex;align-items:center;gap:8px;font-weight:700;color:var(--red);font-size:20px;letter-spacing:1px}
.brand .mark{width:18px;height:18px;background:var(--red)}
.nav a{position:absolute;top:47px;font-size:13px;color:#555;text-decoration:none}
.nav a.active{color:var(--red)}
.btn-red{position:absolute;background:var(--red);color:#fff;font-size:12px;font-weight:600;display:flex;align-items:center;justify-content:center;border-radius:3px}
/* hero */
.hero-city{left:0;top:102px;width:1200px;height:560px;
  background:
    radial-gradient(ellipse 420px 150px at 230px 560px,rgba(214,140,70,.55),rgba(214,140,70,0) 70%),
    radial-gradient(ellipse 520px 120px at 900px 430px,rgba(230,170,100,.28),rgba(230,170,100,0) 70%),
    radial-gradient(ellipse 300px 220px at 180px 200px,rgba(90,70,110,.5),rgba(90,70,110,0) 70%),
    linear-gradient(180deg,var(--dusk-top) 0%,var(--dusk-mid) 38%,#3a2d4a 60%,#4a3428 82%,#6a4426 100%)}
.hero-people{left:590px;top:108px;width:540px;height:550px;
  background:radial-gradient(ellipse 250px 300px at 55% 62%,rgba(22,22,32,.8),rgba(22,22,32,0) 75%)}
.hero-kicker{left:96px;top:296px;font-size:40px;font-weight:200;color:#fff}
.hero-title{left:96px;top:344px;font-size:49px;font-weight:800;color:#fff;letter-spacing:-.3px}
.hero-text{left:97px;top:416px;width:445px;font-size:12.5px;line-height:22px;color:#fff}
.dots{left:98px;top:489px;display:flex;gap:7px}
.dots span{width:9px;height:9px;border:1px solid #fff;border-radius:50%}
.dots span.on{background:#fff}
.seal{position:absolute;width:40px;height:40px;border-radius:50%;background:#fff;border:4px solid var(--red)}
/* headings */
.h-big{font-weight:800;font-size:44px;letter-spacing:-.3px}
.para{font-size:12.5px;line-height:20.6px;color:var(--text)}
/* services */
.card{position:absolute;background:#fff;text-align:center;display:flex;flex-direction:column;align-items:center}
.card .ico{width:82px;height:82px;border-radius:50%;background:var(--red);margin-top:25px;display:flex;align-items:center;justify-content:center}
.card h3{font-size:16px;font-weight:500;margin-top:25px;line-height:21px;color:var(--ink)}
.card p{font-size:12.5px;line-height:20px;color:var(--muted);margin-top:20px;width:250px}
.card.featured{background:linear-gradient(160deg,#a5262a,#8e1418 60%,#7a1216)}
.card.featured .ico{background:#fff;margin-top:42px}
.card.featured h3,.card.featured p{color:#fff}
/* training */
.post{position:absolute;width:290px}
.post .ph{height:265px}
.post h4{font-size:15.5px;font-weight:500;margin:44px 0 0 3px;color:var(--ink)}
.post .meta{display:flex;gap:28px;margin-top:16px;font-size:12.5px;color:var(--red)}
.post .meta span{display:flex;align-items:center;gap:8px}
.post p{font-size:12.5px;line-height:20.6px;color:var(--muted);margin:22px 0 0 3px;width:280px}
.btn-line{margin:23px 0 0 3px;width:111px;height:37px;border:1px solid var(--red);color:var(--red);font-size:12px;font-weight:500;display:flex;align-items:center;justify-content:center;border-radius:3px}
/* contact */
.field{position:absolute;color:#fff;font-size:12.5px;border-bottom:1px solid rgba(255,255,255,.85);padding-bottom:4px}
.info-ico{position:absolute;width:34px;height:34px;border-radius:50%;background:#c21f26;display:flex;align-items:center;justify-content:center}
.info-label{position:absolute;font-size:12px;color:#fff}
.info-val{position:absolute;font-size:16.5px;font-weight:600;color:#fff}
/* footer */
.social{position:absolute;top:3331px;width:20px;height:20px;border-radius:50%;background:var(--red)}
</style>
</head>
<body>

<!-- Header -->
<div class="brand" style="left:103px;top:40px"><span class="mark"></span>VALMIK GROUP</div>
<nav class="nav">
  <a class="active" style="left:624px">Home</a>
  <a style="left:700px">About Us</a>
  <a style="left:789px">Services</a>
  <a style="left:877px">Blue Pike</a>
</nav>
<div class="btn-red" style="left:978px;top:36px;width:111px;height:38px">Contact Us</div>

<!-- Hero -->
<div class="abs hero-city" role="img" aria-label="San Francisco Bay Bridge and city skyline lit up at dusk"></div>
<div class="abs hero-people" role="img" aria-label="Two smiling executives in suits standing back to back"></div>
<svg class="abs" style="left:0;top:640px" width="1200" height="120" aria-hidden="true">
  <polygon points="0,15 600,60 1200,15 1200,120 0,120" fill="#fff"/>
  <polygon points="0,12 600,57 1200,12 1200,26 600,72 0,26" fill="var(--red)"/>
</svg>
<div class="abs hero-kicker">Executive Protection</div>
<div class="abs hero-title">New Era in Protection</div>
<div class="abs hero-text">Contrary to popular belief, Lorem Ipsum is not simply random text. It has roots in a piece of classical Latin literature from</div>
<div class="abs dots"><span></span><span class="on"></span><span></span><span></span></div>
<div class="seal" style="left:580px;top:676px"></div>

<!-- About -->
<svg class="abs" style="left:142px;top:831px" width="346" height="377" role="img" aria-label="Portrait of a man in a suit seated in a car">
  <defs><linearGradient id="aboutPh" x1="0" y1="0" x2="1" y2="1"><stop offset="0" stop-color="#5a5f66"/><stop offset=".5" stop-color="#2b2e33"/><stop offset="1" stop-color="#4d5a3e"/></linearGradient></defs>
  <polygon points="0,0 346,0 346,278 173,377 0,278" fill="url(#aboutPh)"/>
</svg>
<div class="abs h-big" style="left:620px;top:852px">ABOUT US</div>
<div class="abs" style="left:620px;top:919px;font-size:15px;color:var(--red)">Wh We Are</div>
<div class="abs para" style="left:620px;top:962px;width:462px">Donec consectetur blandit sem faucibus dignissim. Interdum et malesuada fames ac ante ipsum primis in faucibus. Phasellus tincidunt vulputate dolor nec varius. Phasellus eget tincidunt turpis. Donec ut mauris iaculis, varius ex non, blandit tellus. Fusce vehicula erat tristique, rhoncus lectus a, facilisis lorem. Integer et bibendum risus. Suspendisse.</div>
<div class="btn-red" style="left:620px;top:1100px;width:111px;height:37px">View More</div>

<!-- Services -->
<svg class="abs" style="left:0;top:1250px" width="1200" height="575" aria-hidden="true">
  <defs><linearGradient id="office" x1="0" y1="0" x2="0" y2="1"><stop offset="0" stop-color="#3a2723"/><stop offset=".6" stop-color="#2a1814"/><stop offset="1" stop-color="#3a1d16"/></linearGradient></defs>
  <polygon points="0,92 600,30 1200,92 1200,574 0,574" fill="url(#office)"/>
  <polygon points="0,82 600,16 1200,82 1200,92 600,36 0,92" fill="var(--red)"/>
</svg>
<div class="abs" role="img" aria-label="Dark wood-panelled executive office" style="left:0;top:1340px;width:1200px;height:484px"></div>
<div class="seal" style="left:580px;top:1262px"></div>
<div class="abs h-big" style="left:0;width:1193px;text-align:center;top:1358px;color:#fff">SERVICES</div>
<div class="abs" style="left:0;width:1196px;text-align:center;top:1415px;font-size:15px;color:#fff">What We Offer</div>

<div class="card" style="left:171px;top:1478px;width:287px;height:265px">
  <div class="ico"><svg width="44" height="44" viewBox="0 0 44 44" fill="none" stroke="#fff" stroke-width="2"><rect x="5" y="6" width="34" height="24" rx="2"/><path d="M18 13l8 5-8 5z"/><path d="M2 36h40"/><circle cx="22" cy="33" r="3"/></svg></div>
  <h3>Executive Protection</h3>
  <p>Contrary to popular belief, Lorem Ipsum is not simply random text.</p>
</div>
<div class="card featured" style="left:458px;top:1461px;width:288px;height:299px">
  <div class="ico"><svg width="48" height="48" viewBox="0 0 48 48" fill="none" stroke="#222" stroke-width="2"><path d="M24 4l11 4v8c0 7-5 11-11 13-6-2-11-6-11-13V8z"/><path d="M19 16l4 4 7-7"/><path d="M4 32l8-3 8 5 6-2 10 6M44 32l-8-3-6 3"/></svg></div>
  <h3>Covert Protection</h3>
  <p>Contrary to popular belief, Lorem Ipsum is not simply random text.</p>
</div>
<div class="card" style="left:746px;top:1478px;width:284px;height:265px">
  <div class="ico"><svg width="44" height="44" viewBox="0 0 44 44" fill="none" stroke="#fff" stroke-width="2"><path d="M16 40V14h-6l10-10 10 10h-6v26"/><path d="M30 40V24h-4l7-7 7 7h-4v16"/></svg></div>
  <h3>Residential Protection &amp;<br>Intelligence</h3>
  <p>Contrary to popular belief, Lorem Ipsum is not simply random text.</p>
</div>

<!-- Training & Consulting -->
<div class="abs h-big" style="left:0;width:1200px;text-align:center;top:1920px">TRAINING <span style="color:var(--red)">&amp;</span> CONSULTING</div>
<div class="abs para" style="left:270px;width:660px;text-align:center;top:2007px;color:var(--muted)">Donec consectetur blandit sem faucibus dignissim. Interdum et malesuada fames ac ante ipsum primis in faucibus. Phasellus tincidunt vulputate dolor nec varius.</div>

<div class="post" style="left:146px;top:2105px">
  <div class="ph" role="img" aria-label="Two businessmen reviewing a tablet" style="background:linear-gradient(135deg,#e8ecf0,#8894a6 55%,#2d3a5a)"></div>
  <h4>Ledgerline Financial Solutions</h4>
  <div class="meta"><span><svg width="16" height="16" viewBox="0 0 16 16" fill="none" stroke="#8e1418"><circle cx="8" cy="8" r="6.5"/></svg>2 Comments</span><span><svg width="16" height="16" viewBox="0 0 16 16" fill="none" stroke="#8e1418"><circle cx="8" cy="5" r="3.5"/><path d="M2 15c0-4 3-5 6-5s6 1 6 5"/></svg>By Daniel</span></div>
  <p>Contrary to popular belief, Lorem Ipsum is not simply random text. It has roots in a piece of classical Latin</p>
  <div class="btn-line">View More</div>
</div>
<div class="post" style="left:459px;top:2105px">
  <div class="ph" role="img" aria-label="Businesswoman in glasses seated at a desk" style="background:linear-gradient(135deg,#d9d3c6,#8a7a62 55%,#2a2c44)"></div>
  <h4>Gender Diversity</h4>
  <div class="meta"><span><svg width="16" height="16" viewBox="0 0 16 16" fill="none" stroke="#8e1418"><circle cx="8" cy="8" r="6.5"/></svg>2 Comments</span><span><svg width="16" height="16" viewBox="0 0 16 16" fill="none" stroke="#8e1418"><circle cx="8" cy="5" r="3.5"/><path d="M2 15c0-4 3-5 6-5s6 1 6 5"/></svg>By Daniel</span></div>
  <p>Contrary to popular belief, Lorem Ipsum is not simply random text. It has roots in a piece of classical Latin</p>
  <div class="btn-line">View More</div>
</div>
<div class="post" style="left:773px;top:2105px">
  <div class="ph" role="img" aria-label="Senior executive in a meeting with a colleague" style="background:linear-gradient(135deg,#b8c2cc,#5d6672 55%,#2c3038)"></div>
  <h4>Officials in Meeting</h4>
  <div class="meta"><span><svg width="16" height="16" viewBox="0 0 16 16" fill="none" stroke="#8e1418"><circle cx="8" cy="8" r="6.5"/></svg>2 Comments</span><span><svg width="16" height="16" viewBox="0 0 16 16" fill="none" stroke="#8e1418"><circle cx="8" cy="5" r="3.5"/><path d="M2 15c0-4 3-5 6-5s6 1 6 5"/></svg>By Daniel</span></div>
  <p>Contrary to popular belief, Lorem Ipsum is not simply random text. It has roots in a piece of classical Latin</p>
  <div class="btn-line">View More</div>
</div>

<!-- Contact -->
<svg class="abs" style="left:0;top:2700px" width="1200" height="580" aria-hidden="true">
  <defs>
    <linearGradient id="boardroom" x1="0" y1="0" x2="0" y2="1"><stop offset="0" stop-color="#3a3a3c"/><stop offset=".5" stop-color="#222"/><stop offset="1" stop-color="#0c0c0c"/></linearGradient>
    <linearGradient id="redPanel" x1="0" y1="0" x2="0" y2="1"><stop offset="0" stop-color="#93161b"/><stop offset="1" stop-color="#7e1115"/></linearGradient>
  </defs>
  <polygon points="0,96 600,20 1200,96 1200,102 600,34 0,102" fill="#000"/>
  <polygon points="0,102 597,34 597,578 0,578" fill="url(#boardroom)"/>
  <polygon points="597,34 1200,102 1200,578 597,578" fill="url(#redPanel)"/>
</svg>
<div class="abs" role="img" aria-label="Empty boardroom with leather chairs" style="left:0;top:2810px;width:597px;height:468px"></div>
<div class="seal" style="left:580px;top:2716px"></div>
<div class="abs h-big" style="left:131px;top:2902px;color:#fff">CONTACT US</div>
<div class="abs" style="left:133px;top:2967px;font-size:12.5px;color:#fff">Contrary to popular belief, Lorem</div>

<div class="info-ico" style="left:137px;top:3039px"><svg width="16" height="16" viewBox="0 0 24 24" fill="#fff"><path d="M6.6 10.8a15 15 0 006.6 6.6l2.2-2.2a1 1 0 011-.25 11.4 11.4 0 003.6.57 1 1 0 011 1V20a1 1 0 01-1 1A17 17 0 013 4a1 1 0 011-1h3.5a1 1 0 011 1c0 1.25.2 2.45.57 3.6a1 1 0 01-.25 1z"/></svg></div>
<div class="info-label" style="left:190px;top:3037px">Phone Number</div>
<div class="info-val" style="left:190px;top:3054px">(+123) 456 789</div>
<div class="info-ico" style="left:137px;top:3119px"><svg width="16" height="16" viewBox="0 0 24 24"><path d="M2 5h20v14H2z" fill="none" stroke="#fff" stroke-width="2"/><path d="M2 6l10 7 10-7" fill="none" stroke="#fff" stroke-width="2"/></svg></div>
<div class="info-label" style="left:190px;top:3117px">Email Address</div>
<div class="info-val" style="left:190px;top:3134px">info@valmikgroup.com</div>

<div class="field" style="left:662px;top:2926px;width:186px">First Name</div>
<div class="field" style="left:886px;top:2926px;width:203px">Last Name</div>
<div class="field" style="left:662px;top:2979px;width:186px">Email address</div>
<div class="field" style="left:886px;top:2979px;width:203px">Phone</div>
<div class="field" style="left:662px;top:3037px;width:427px;height:37px">Message</div>
<div class="abs" style="left:963px;top:3103px;width:126px;height:36px;background:#fff;color:var(--ink);font-size:12px;font-weight:500;display:flex;align-items:center;justify-content:center;border-radius:3px">Send Message</div>

<!-- Footer -->
<span class="social" style="left:146px" aria-label="Social link"></span>
<span class="social" style="left:181px" aria-label="Social link"></span>
<span class="social" style="left:218px" aria-label="Social link"></span>
<span class="social" style="left:254px" aria-label="Social link"></span>
<span class="social" style="left:289px" aria-label="Social link"></span>
<div class="brand" style="left:526px;top:3327px"><span class="mark"></span>VALMIK GROUP</div>
<div class="abs" style="left:760px;width:315px;text-align:right;top:3332px;font-size:12px;color:#555">© 2021 <span style="color:var(--red)">Valmik Group</span>. All rights reserved.</div>

</body>
</html>
```